Design of labels for exciting new natural skincare products...natural deodorant

I need some labels designed for a range of natural skincare, initially a natural deodorant paste. i will be offering a range of fragrances so i want a basic idea that i can drop different colours / ingredients into easily.

Fragrances are:
1. Jasmine, Orange and Bergamot
2. Lavender & Bergamot
3. Peppermint & Tea tree
4. Unscented
5. Lime, Lemongrass & Ginger

I am a new startup and will be selling online and through a couple of specialty online stores. The final design should encompass our ethos which is clean and green, not fussy nor clinical but friendly and easily accessible. I like fresh, contemporary modern look referencing vintage aesthetics.

The idea is that these products are better for your body AND the environment, and we pledge to use no plastic to package or distribute our products. i like the use of contemporary pastels such as soft pinks, tans and green/blue/aquas, though am open to new ideas too. the logo (attached) appears in red but that should not necessarily be used. i also like black and white with touches of colour.

Target Market(s)

Eco aware, health concious consumers with a reasonable skincare budget.

Industry/Entity Type

Skin Care Product

Font styles to use
Serif
Sans Serif
Decorative

Colors
2eb6a2
b768aa
eea4c8
fabb94
85cae6
cfeae6
eaf2ce
000000
eaeaea

Requirements
Must have
• Labels are for a small glass jar - the dimensions are 2cm high only and wrapping around the jar - at least 10cm wide. i'm also going to be providing a smaller size so this needs to be able to scale down to 1.5cm high and 8cm wide.
• the logo (supplied)
• title: Natural Deodorant
• Subtitle: Orange, Jasmine & Bergamot
• 45g
• Ingredients: tapioca starch*, bicarbonate of soda, Coconut oil*, shea butter*, mango butter*, diatomaceous earth*, sweet almond oil*, vitamin e*, tea tree oil*, Sweet orange essential oil*, Jasmine essential oil*, Bergamot essential oil*.
• *Certified organic ingredient
• (DESIGNERS - PLEASE NOTE NOT ALL THE INGREDIENTS ARE ORGANIC, PLEASE LIST THEM WITH A STAR * IF I HAVE SUPPLIED IT, THEN *Certified organic ingredient BELOW IN SLIGHTLY SMALLER TEXT - THIS SERVES AS THE KEY FOR THE INGREDIENTS LIST)
• wrenmeadow.nz
• Massage a pea-sized amount onto clean, dry armpits for an odour-free day.
• If irritation develops discontinue use and contact Wren Meadow. (please italicise the company name)
Nice to have
• open to ideas - i am attaching some examples of designs i like, you'll notice i swing between plain black and white aesthetics and a more decorative look. In general i like the old "medicine bottle" look, with hand sketched illustrations. But i'm open to ideas!

```html
<!DOCTYPE html>
<html lang="en">
<head>
<meta charset="utf-8">
<title>Wren Meadow Natural Deodorant Label</title>
<link rel="stylesheet" href="https://fonts.googleapis.com/css2?family=Oswald:wght@300;400;500&family=Dancing+Script:wght@600&family=Open+Sans:wght@400;700&display=swap">
<style>
  :root {
    --page: #f4f4f4;
    --aqua: #cfeae6;
    --aqua-deep: #b9e2db;
    --blush: #f7b9ad;
    --blush-deep: #f3a597;
    --teal: #2eb6a2;
    --plum: #b768aa;
    --ink: #2b2b2b;
    --paper: #ffffff;
    --paper-soft: #fafafa;
    --rule: #b768aa;
    --badge: #6f6f6f;
  }
  * { box-sizing: border-box; margin: 0; padding: 0; }
  html, body { width: 1134px; height: 1200px; overflow: hidden; }
  body { background: var(--page); position: relative; font-family: "Oswald", sans-serif; }

  .label {
    position: absolute; left: 37px; top: 494px;
    width: 1060px; height: 212px;
    display: flex;
    box-shadow: 0 10px 18px rgba(0,0,0,0.12);
  }

  .label-front { position: relative; width: 530px; height: 100%; overflow: hidden; }
  .front-backdrop {
    position: absolute; inset: 0;
    background:
      linear-gradient(155deg, transparent 62%, var(--blush) 62%),
      linear-gradient(90deg, var(--aqua) 0 55%, var(--blush-deep) 55%);
  }
  .title-card {
    position: absolute; left: 127px; top: 22px; width: 275px; height: 167px;
    background: var(--paper-soft);
    border: 2px solid #f6c9c1;
    text-align: center;
  }
  .brand-row { position: absolute; left: 28px; top: 16px; display: flex; align-items: center; gap: 12px; }
  .organic-seal { width: 40px; height: 40px; border-radius: 50%; background: var(--badge); }
  .brand-name { font-family: "Oswald", sans-serif; font-weight: 500; font-size: 27px; color: var(--teal); letter-spacing: 0.5px; }
  .product-title {
    position: absolute; left: 0; right: 0; top: 72px;
    font-weight: 300; font-size: 27px; color: var(--ink); letter-spacing: -0.3px;
  }
  .scent-band {
    position: absolute; left: 35px; top: 110px; width: 205px; height: 26px;
    background: var(--plum);
    clip-path: polygon(0 0, 100% 0, 97% 100%, 3% 100%);
    color: var(--paper); font-family: "Open Sans", sans-serif; font-size: 13px; line-height: 26px;
  }
  .net-weight {
    position: absolute; left: 0; right: 0; top: 142px;
    font-family: "Open Sans", sans-serif; font-weight: 700; font-size: 12px; color: var(--ink);
  }

  .label-back { position: relative; width: 530px; height: 100%; background: var(--paper); }
  .back-heading {
    position: absolute; left: 0; right: 0; top: 14px; text-align: center;
    font-family: "Dancing Script", cursive; font-size: 27px; color: var(--plum);
  }
  .ingredient-list {
    position: absolute; left: 40px; right: 40px; top: 52px; text-align: center;
    font-weight: 300; font-size: 13.5px; line-height: 18px; color: var(--ink);
  }
  .back-rule { position: absolute; left: 56px; right: 44px; top: 131px; border-top: 1px solid var(--rule); }
  .directions {
    position: absolute; left: 56px; top: 140px; width: 260px;
    font-weight: 400; font-size: 13.5px; line-height: 16px; color: var(--teal);
  }
  .marks { position: absolute; right: 44px; top: 142px; display: flex; gap: 12px; align-items: center; }
  .mark { width: 34px; height: 32px; background: var(--badge); border-radius: 4px; }
  .mark.round { width: 32px; border-radius: 50%; background: var(--ink); }
  .web-tab {
    position: absolute; left: 150px; bottom: 0; width: 246px; height: 28px;
    background: var(--plum); border-radius: 14px 14px 0 0;
    color: var(--paper); text-align: center; line-height: 28px;
    font-size: 14px; letter-spacing: 1.5px;
  }
</style>
</head>
<body>
  <div class="label">
    <section class="label-front">
      <div class="front-backdrop" role="img" aria-label="Soft aqua and blush pink marbled backdrop"></div>
      <div class="title-card">
        <div class="brand-row">
          <span class="organic-seal" role="img" aria-label="Certified organic ingredients seal"></span>
          <span class="brand-name">Wren Meadow</span>
        </div>
        <h1 class="product-title">NATURAL DEODORANT</h1>
        <div class="scent-band">Orange, Jasmine &amp; Bergamot</div>
        <div class="net-weight">45G</div>
      </div>
    </section>

    <section class="label-back">
      <h2 class="back-heading">Ingredients</h2>
      <p class="ingredient-list">Coconut oil*, tapioca starch*, bicarbonate of soda, shea butter*, mango butter*, diatomaceous earth*, sweet almond oil*, vitamin e*, tea tree oil*, Sweet orange essential oil*, Jasmine essential oil*, Bergamot essential oil*.</p>
      <div class="back-rule"></div>
      <p class="directions">Massage a pea-sized amount onto clean, dry armpits for an odour-free day.</p>
      <div class="marks">
        <span class="mark" role="img" aria-label="Not tested on animals badge"></span>
        <span class="mark" role="img" aria-label="Made in New Zealand badge"></span>
        <span class="mark round" role="img" aria-label="Recyclable badge"></span>
      </div>
      <div class="web-tab">WWW.WRENMEADOW.NZ</div>
    </section>
  </div>
</body>
</html>
```